Letterhead/Envelope/Business Cards for law firm - Marlowe & Tesniere PLLC
Marlowe Tesniere
Letterhead/Envelope/Business Cards for law firm - Marlowe & Tesniere PLLC - Law
Creative Brief
Use same font as used in my logo
Open to any ideas
Simple
Doran P. Tesniere
Attorney
Marlowe & Tesniere PLLC 618 Briarmoss Court Plaza 375 North Galloway Avenue Louisville, Kentucky 40597
dtesniere@mtlegalgroup.example
www.mtlegalgroup.example
Licensed in Kentucky, Indiana & West Virginia
We are looking for design of letterhead, envelopes and business cards.
We want to use our logo. But we also need Marlowe & Tesniere, PLLC on the card/letterhead.

```html
<!DOCTYPE html>
<html lang="en">
<head>
<meta charset="utf-8">
<title>Marlowe &amp; Tesniere PLLC — Business Card</title>
<link href="https://fonts.googleapis.com/css2?family=Cinzel:wght@400;600&display=swap" rel="stylesheet">
<style>
  :root {
    --backdrop: #e6e4e1;
    --card: #ffffff;
    --ink: #1a1a1a;
    --accent: #e0222c;
    --muted: #444444;
  }
  * { margin: 0; padding: 0; box-sizing: border-box; }
  html, body {
    width: 1200px; height: 900px; overflow: hidden;
    background: var(--backdrop);
  }
  .canvas {
    width: 1200px; height: 900px;
    display: flex; align-items: center; justify-content: center;
  }
  .business-card {
    position: relative;
    width: 1000px; height: 571px;
    background: var(--card);
    box-shadow: 0 6px 24px rgba(0,0,0,0.18);
    overflow: hidden;
    font-family: "Cinzel", serif;
    color: var(--ink);
  }
  .firm-wordmark {
    position: absolute;
    right: 52px; top: 48px;
    font-size: 52px;
    font-weight: 400;
    letter-spacing: 3px;
    text-transform: uppercase;
    color: var(--ink);
    white-space: nowrap;
  }
  .firm-mark {
    position: absolute;
    left: 40px; top: 210px;
    width: 240px; height: 240px;
    border-radius: 50%;
    background: var(--accent);
  }
  .attorney {
    position: absolute;
    right: 52px; top: 150px;
    text-align: right;
  }
  .attorney-name {
    font-size: 30px;
    font-weight: 600;
    color: var(--accent);
    letter-spacing: 1px;
  }
  .attorney-title {
    font-size: 22px;
    color: var(--ink);
    margin-top: 4px;
    letter-spacing: 1px;
  }
  .contact-list {
    position: absolute;
    right: 52px; top: 262px;
    list-style: none;
    text-align: right;
    font-size: 15px;
    line-height: 23px;
    color: var(--muted);
    letter-spacing: 0.5px;
  }
  .contact-list li {
    display: flex; align-items: center; justify-content: flex-end; gap: 10px;
  }
  .contact-icon {
    width: 13px; height: 13px; border-radius: 50%;
    background: var(--accent);
    flex: none;
  }
  .online-list {
    position: absolute;
    right: 75px; top: 450px;
    list-style: none;
    text-align: right;
    font-size: 14px;
    line-height: 21px;
    color: var(--muted);
    letter-spacing: 0.5px;
    text-transform: uppercase;
  }
</style>
</head>
<body>
<main class="canvas">
  <article class="business-card">
    <div class="firm-mark" aria-hidden="true"></div>
    <h1 class="firm-wordmark">Marlowe Tesniere</h1>

    <section class="attorney">
      <p class="attorney-name">Doran P. Tesniere</p>
      <p class="attorney-title">Attorney</p>
    </section>

    <ul class="contact-list">
      <li>618 Briarmoss Court Plaza <span class="contact-icon"></span></li>
      <li>375 North Galloway Avenue <span class="contact-icon"></span></li>
      <li>Louisville, Kentucky 40597 <span class="contact-icon"></span></li>
      <li>502-555-0148 <span class="contact-icon"></span></li>
      <li>502-555-0173 <span class="contact-icon"></span></li>
      <li>502-555-0126 <span class="contact-icon"></span></li>
    </ul>

    <ul class="online-list">
      <li>dtesniere@mtlegalgroup.example</li>
      <li>www.mtlegalgroup.example</li>
    </ul>
  </article>
</main>
</body>
</html>
```